2 guided dives on the North of Bonaire

2 guided shore dives on the North of Bonaire including authentic local lunch and drinks.
We offer an adventure for experienced divers to discover the dive sites on the north of the island.
Showing you the beauty of the reefs and tasting authentic local cuisine like goat or iguana combined with a stunning view of the surroundings.

Target Market(s)

Divers / tourism

Industry/Entity Type

Tourism / Diving

Font styles to use
Sans Serif

Colors
0054AA
0677BA
7BADD7
CADEEF
E8F1F8
0094D4
00A9DD
6FCCEA
C7EBF8
E9F6FB
F0912C
F2A743
F7CA91
FBE8D2
FDF5EE
EE7325
F08F49
F5BC92
FAE3D3
FDF4ED

Requirements
Must have
• Some of the pictures I uploaded and the food picture / bottom like in the pictures
Nice to have
• inviting to join us on the guided dives
Should not have
• Any picture I didn't provide

```html
<!DOCTYPE html>
<html lang="en">
<head>
<meta charset="utf-8">
<title>Let Us Guide You – Guided Dives North Bonaire</title>
<link rel="stylesheet" href="https://fonts.googleapis.com/css2?family=Poppins:ital,wght@0,400;0,500;0,600;0,800;0,900;1,600&display=swap">
<style>
  :root{
    --page:#454545;
    --navy:#142b4c;
    --band-blue:#0e69b0;
    --url-blue:#0677BA;
    --orange:#F2A743;
    --ink:#111418;
    --white:#ffffff;
    --sky-top:#4469b2;
    --sky-mid:#5f8fd0;
    --sky-low:#86b3e2;
  }
  *{box-sizing:border-box;margin:0;padding:0}
  html,body{width:1076px;height:1200px;overflow:hidden;background:var(--page);font-family:'Poppins',sans-serif}
  .flyer{position:absolute;left:197px;top:116px;width:683px;height:967px;overflow:hidden;background:var(--navy);box-shadow:0 6px 18px rgba(0,0,0,.4)}
  .hero-photo{position:absolute;left:0;top:0;width:683px;height:770px;
    background:linear-gradient(180deg,var(--sky-top) 0%,var(--sky-mid) 35%,var(--sky-low) 49%,#5d86a8 55%,#3f7f92 65%,#6c9aa4 74%,#9b9c97 84%,#b3b0aa 100%)}
  .badge{position:absolute;left:62px;top:0;width:88px;height:160px;background:var(--white);border-radius:0 0 44px 44px}
  .badge-mark{position:absolute;left:11px;top:46px;width:66px;height:66px;border-radius:50%;background:var(--url-blue)}
  .headline{position:absolute;right:35px;top:62px;text-align:right;font-weight:900;line-height:85px;letter-spacing:-2px;white-space:nowrap}
  .headline .line{display:block;font-size:80px}
  .headline .white{color:var(--white);text-shadow:-4px 4px 0 var(--ink)}
  .headline .accent{color:var(--orange);text-shadow:-4px 4px 0 var(--ink)}
  .subtitle{position:absolute;right:33px;top:240px;font-size:20px;font-weight:500;color:var(--ink);white-space:nowrap}
  .promise-band{position:absolute;left:181px;top:380px;width:502px;height:72px;background:var(--band-blue)}
  .promise{position:absolute;right:33px;color:var(--white);font-weight:600;font-size:15px;line-height:20px;display:flex;align-items:center;gap:7px;white-space:nowrap}
  .promise svg{width:17px;height:14px}
  .promise.one{top:12px}.promise.two{top:36px}
  .lunch-band{position:absolute;left:323px;top:453px;width:360px;height:32px;background:var(--orange);
    display:flex;align-items:center;padding-left:17px;font-style:italic;font-weight:600;font-size:10.5px;color:var(--ink);letter-spacing:.2px;white-space:nowrap}
  .polaroid{position:absolute;background:var(--white);padding:7px 7px 26px;box-shadow:0 4px 10px rgba(0,0,0,.35)}
  .polaroid .photo{width:100%;height:100%}
  .p1{left:-6px;top:608px;width:170px;height:186px;transform:rotate(-4deg)}
  .p2{left:153px;top:606px;width:182px;height:183px;transform:rotate(2deg)}
  .p3{left:322px;top:606px;width:198px;height:186px;transform:rotate(-3deg)}
  .p4{left:503px;top:612px;width:186px;height:177px;transform:rotate(-1deg)}
  .food{background:linear-gradient(135deg,#d9893e,#9c4a26 55%,#c99355)}
  .beach{background:linear-gradient(180deg,#4b7fc4 0%,#8cb8e2 48%,#3fb2c4 58%,#e7dcc6 70%,#d9cdb6 100%)}
  .seahorse{background:linear-gradient(120deg,#1a7d8e,#8a2b3a 40%,#2a8fa0 65%,#0f5b6a)}
  .landscape{background:linear-gradient(180deg,#4a7ecb 0%,#9dbfe6 38%,#2f66b0 52%,#3d7a45 75%,#6e8f4e 100%)}
  .social{position:absolute;left:381px;top:816px;display:flex;align-items:center;gap:7px;color:var(--white);font-size:13px;line-height:20px;white-space:nowrap}
  .social .dot{width:18px;height:18px;border-radius:50%;background:var(--orange)}
  .brand{position:absolute;left:30px;top:886px;display:flex;align-items:center;gap:8px;color:var(--orange);font-weight:800;font-size:20px;line-height:1;white-space:nowrap}
  .brand .dot{width:20px;height:20px;border-radius:50%;background:var(--orange)}
  .call-box{position:absolute;left:236px;top:860px;width:225px;height:32px;background:var(--orange);border-radius:5px;
    display:flex;align-items:center;padding-left:12px;gap:8px;font-weight:500;font-size:14px;color:var(--ink);white-space:nowrap}
  .call-box svg{width:14px;height:14px}
  .web-box{position:absolute;left:236px;top:899px;width:414px;height:29px}
  .web-box .label{position:absolute;left:0;top:0;width:197px;height:100%;background:var(--orange);clip-path:polygon(0 0,100% 0,94% 100%,0 100%);
    display:flex;align-items:center;padding-left:13px;font-weight:500;font-size:14px;color:var(--ink);white-space:nowrap}
  .web-box .url{position:absolute;left:185px;right:0;top:0;bottom:0;background:var(--url-blue);clip-path:polygon(6% 0,100% 0,100% 100%,0 100%);
    display:flex;align-items:center;justify-content:flex-end;padding-right:18px;color:var(--white);font-size:16px;white-space:nowrap}
  .contact{position:absolute;left:474px;color:var(--white);display:flex;align-items:center;gap:7px;white-space:nowrap}
  .contact.address{top:858px;font-size:7.5px;line-height:12px}
  .contact.email{top:872px;font-size:14px;line-height:20px}
  .contact svg{width:11px;height:11px}
</style>
</head>
<body>
<main class="flyer">
  <div class="hero-photo" role="img" aria-label="Rocky coastline on the north side of Bonaire with turquoise sea and blue sky"></div>

  <div class="badge" aria-label="Dive certification partner badge"><div class="badge-mark"></div></div>

  <h1 class="headline">
    <span class="line white">LET US</span>
    <span class="line accent">GUIDE YOU!</span>
  </h1>
  <p class="subtitle">2 GUIDED DIVES AT THE NORTH SIDE OF BONAIRE</p>

  <div class="promise-band">
    <p class="promise one">We show you the cool stuff
      <svg viewBox="0 0 20 16" fill="none" stroke="#fff" stroke-width="3" stroke-linejoin="round"><polyline points="9,2 3,8 9,14"/><polyline points="17,2 11,8 17,14"/></svg></p>
    <p class="promise two">You just enjoy the dives, we take care of the rest
      <svg viewBox="0 0 20 16" fill="none" stroke="#fff" stroke-width="3" stroke-linejoin="round"><polyline points="9,2 3,8 9,14"/><polyline points="17,2 11,8 17,14"/></svg></p>
  </div>
  <p class="lunch-band">AUTHENTIC LOCAL LUNCH AND DRINKS AT KAS DI MIRA</p>

  <figure class="polaroid p1"><div class="photo food" role="img" aria-label="Plates of authentic local Bonaire food"></div></figure>
  <figure class="polaroid p2"><div class="photo beach" role="img" aria-label="White sand beach under a palm-leaf shade"></div></figure>
  <figure class="polaroid p3"><div class="photo seahorse" role="img" aria-label="Seahorse clinging to red coral underwater"></div></figure>
  <figure class="polaroid p4"><div class="photo landscape" role="img" aria-label="Lagoon with cacti and green hills"></div></figure>

  <p class="social"><span class="dot"></span>/ReefsideDiveBonaire</p>

  <div class="brand"><span class="dot"></span>Reefside Dive</div>

  <div class="call-box">CALL US
    <svg viewBox="0 0 16 16"><circle cx="8" cy="8" r="8" fill="#fff"/><path d="M5 4.5l1.6-.5 1 2.2-1 .8c.5 1 1.3 1.8 2.3 2.3l.8-1 2.2 1-.5 1.6c-3.3.2-6.6-3.1-6.4-6.4z" fill="#0677BA"/></svg>
    +(599) 700 1234</div>

  <div class="web-box">
    <span class="label">VISIT OUR WEBSITE</span>
    <span class="url">www.reefside-dive.com</span>
  </div>

  <p class="contact address"><svg viewBox="0 0 12 12"><path d="M6 0a4 4 0 0 0-4 4c0 3 4 8 4 8s4-5 4-8a4 4 0 0 0-4-4zm0 5.5a1.5 1.5 0 1 1 0-3 1.5 1.5 0 0 1 0 3z" fill="#fff"/></svg>Kaya Koral 12, Kralendijk, Bonaire</p>
  <p class="contact email"><svg viewBox="0 0 12 12"><rect x="0" y="2" width="12" height="8" fill="#fff"/><polyline points="0,2 6,7 12,2" fill="none" stroke="#142b4c" stroke-width="1.2"/></svg>hello@reefside-dive.com</p>
</main>
</body>
</html>
```